SilverLedgerOak - Double Sided Business Card

We are looking for design options or our business cards. We are a Business Solutions and HR solutions Provider - the theme is business, for this card.

Our brand colours are represented within our logo.

Details needed to be put on the front of the business card are:

Employees name: [Sample Name]
Role: [Sample Role]

Address: Suite 4 - Level 3/48 Halloran Avenue Parramatta NSW 2150
M: 0000 000 000
P: 1300 847 213
F: 1300 847 286
E: sample@silverledgeroak.com.au
www.silverledgeroak.com.au
Updates

Reason: Hello, could we please increase our deadline by 5 days. Thanking you, Tess

Target Market(s)

Business Owners, also Candidates looking for Employment

Industry/Entity Type

Business

Contact Information for Business Card

Role: [Sample Role]

M: 0000 000 000
P: 1300 847 213
F: 1300 847 286

Font styles to use
Sans Serif

Colors
3276b5
3176b5
0455a3
85abd2
cfdeed
ffffff
000000
1b1b1b
757575

Requirements
Must have
• Details needed to be put on the front of the business card are:
• Employees name: [Sample Name]
• Role: [Sample Role]
• Address: Suite 4 - Level 3/48 Halloran Avenue Parramatta NSW 2150
• M: 0000 000 000
• P: 1300 847 213
• F: 1300 847 286
• E: sample@silverledgeroak.com.au
• www.silverledgeroak.com.au
Nice to have
• Simplicity, clean and professional.

```html
<!DOCTYPE html>
<html lang="en">
<head>
<meta charset="utf-8">
<title>SilverLedgerOak – Business Card</title>
<link href="https://fonts.googleapis.com/css2?family=Orbitron:wght@700&family=Roboto:ital,wght@0,400;0,700;1,400&display=swap" rel="stylesheet">
<style>
  :root {
    --navy: #12284a;
    --brand-blue: #0455a3;
    --paper: #f4f4f4;
    --ink: #3a3a3a;
    --ink-dark: #1b1b1b;
    --white: #ffffff;
    --backdrop: #e6e6e6;
  }
  * { margin: 0; padding: 0; box-sizing: border-box; }
  html, body {
    width: 1200px; height: 960px; overflow: hidden;
    background: var(--backdrop);
  }
  .canvas { position: relative; width: 1200px; height: 960px; }

  .card {
    position: absolute;
    width: 600px; height: 343px;
    box-shadow: 0 2px 5px rgba(0,0,0,.25);
  }

  /* Front */
  .card-front { left: 314px; top: 113px; background: var(--paper); }
  .accent-bar-left {
    position: absolute; left: 0; top: 59px; width: 12px; height: 224px;
    background: var(--navy);
  }
  .accent-bar-right {
    position: absolute; right: 0; top: 221px; width: 12px; height: 62px;
    background: var(--brand-blue);
  }
  .person { position: absolute; left: 44px; top: 62px; }
  .person-name {
    font-family: 'Orbitron', sans-serif; font-weight: 700;
    font-size: 20px; letter-spacing: 1.5px; color: var(--navy); line-height: 24px;
  }
  .person-role {
    font-family: 'Orbitron', sans-serif; font-weight: 700;
    font-size: 12px; letter-spacing: .8px; color: var(--brand-blue); line-height: 16px;
  }
  .person-email {
    margin-top: 4px;
    font-family: 'Roboto', sans-serif; font-style: italic;
    font-size: 14px; color: var(--ink); line-height: 18px;
  }
  .contact-list {
    position: absolute; left: 44px; top: 138px; list-style: none;
    font-family: 'Roboto', sans-serif; font-size: 14px; color: var(--ink); line-height: 19px;
  }
  .contact-list li { display: flex; align-items: center; gap: 8px; }
  .contact-list svg { width: 14px; height: 14px; fill: var(--ink-dark); }
  .address {
    position: absolute; left: 44px; top: 208px;
    font-family: 'Roboto', sans-serif; font-size: 14px; color: var(--ink); line-height: 18.5px;
    font-style: normal;
  }
  .address .web { font-weight: 700; color: var(--ink-dark); }

  .brand-lockup {
    position: absolute; left: 336px; top: 210px; width: 218px;
    display: flex; align-items: center; justify-content: center; gap: 8px;
  }
  .brand-square { width: 14px; height: 14px; background: var(--navy); }
  .brand-name {
    font-family: 'Roboto', sans-serif; font-weight: 700;
    font-size: 22px; color: var(--brand-blue); letter-spacing: .3px;
  }

  /* Back */
  .card-back { left: 311px; top: 472px; background: var(--navy); }
  .back-brand {
    position: absolute; left: 0; right: 0; top: 140px;
    text-align: center;
    font-family: 'Roboto', sans-serif; font-weight: 700;
    font-size: 40px; color: var(--white);
  }
  .back-web {
    position: absolute; left: 0; right: 0; top: 300px;
    text-align: center;
    font-family: 'Roboto', sans-serif; font-size: 14px;
    letter-spacing: 3px; color: var(--white);
  }
</style>
</head>
<body>
<main class="canvas">

  <section class="card card-front" aria-label="Business card front">
    <div class="accent-bar-left"></div>
    <div class="accent-bar-right"></div>

    <div class="person">
      <h1 class="person-name">DANIEL HARPER</h1>
      <p class="person-role">CEO/FOUNDER</p>
      <p class="person-email">sample@silverledgeroak.com.au</p>
    </div>

    <ul class="contact-list">
      <li>
        <svg viewBox="0 0 24 24" aria-label="Phone"><path d="M6.6 10.8a15.1 15.1 0 0 0 6.6 6.6l2.2-2.2c.3-.3.7-.4 1-.2 1.1.4 2.3.6 3.6.6.6 0 1 .4 1 1V20c0 .6-.4 1-1 1C10.6 21 3 13.4 3 4c0-.6.4-1 1-1h3.5c.6 0 1 .4 1 1 0 1.3.2 2.5.6 3.6.1.3 0 .7-.2 1z"/></svg>
        1300 847 213
      </li>
      <li>
        <svg viewBox="0 0 24 24" aria-label="Mobile"><path d="M7 1h10a2 2 0 0 1 2 2v18a2 2 0 0 1-2 2H7a2 2 0 0 1-2-2V3a2 2 0 0 1 2-2zm0 3v14h10V4z"/></svg>
        0000 000 000
      </li>
      <li>
        <svg viewBox="0 0 24 24" aria-label="Fax"><path d="M6 2h12v6H6zM3 9h18a1 1 0 0 1 1 1v9a1 1 0 0 1-1 1H3a1 1 0 0 1-1-1v-9a1 1 0 0 1 1-1zm3 6v5h12v-5z"/></svg>
        1300 847 286
      </li>
    </ul>

    <address class="address">
      Suite 4 - Level 3/48<br>
      Halloran Avenue<br>
      Parramatta NSW 2150<br>
      <span class="web">www.silverledgeroak.com.au</span>
    </address>

    <div class="brand-lockup">
      <span class="brand-square"></span>
      <span class="brand-name">SilverLedgerOak</span>
    </div>
  </section>

  <section class="card card-back" aria-label="Business card back">
    <p class="back-brand">SilverLedgerOak</p>
    <p class="back-web">www.silverledgeroak.com.au</p>
  </section>

</main>
</body>
</html>
```